"MEET THE TEAM" page web design

We need a "meet the team" page for our website!
Please look at our website to see the style we need

We are looking for something unique, fun, cool, technology-style and yet professional. We plan on taking a picture of each employee (not sure if this will be a real photo/caricature/ black and white/goofy picture--> but we are open to any ideas you have that will work with the design) and putting it there, along with a little bio about each person.

Thanks! looking forward to working together:)
Updates

Project Deadline Extended
Reason: I am excited to see more designs and find the perfect fit. Thanks designers :)

Target Market(s)

People looking to purchase servers, workstations, components

Industry/Entity Type

Information Technology

Number of Pages Required

1 page

Font styles to use
Sans Serif
Other font styles liked:
• The font we use on our site so it matches

Requirements
Must have
• please look at our website qondimex.com and see the theme and colors we want.
• We have 13 employees but would like to have a design where we can add/remove people if we hire/terminate them without messing up the design.
• We are looking for something unique, fun, cool, technology-style and yet professional. We plan on taking a picture of each employee (not sure if this will be a real photo/caricature/ black and white/goofy picture--> but we are open to any ideas you have that will work with the design) and putting it there, along with a little bio about each person.
• We can upload anything you need
Nice to have
• We are also interested in having a design where when the cursor moves over a person then the bio comes out or moves around, or something. (This is not required, but we would love some cool ideas) And if you can come up with some design, we would have our programmers create it for us.
Should not have
• we are open to anything

```html
<!DOCTYPE html>
<html lang="en">
<head>
<meta charset="utf-8">
<title>Qondimex – Meet the Team</title>
<link href="https://fonts.googleapis.com/css2?family=Arimo:wght@400;700&display=swap" rel="stylesheet">
<style>
:root{
  --teal:#2aa7a0;
  --teal-light:#3dbab3;
  --ink:#1d2b2b;
  --text:#555d5d;
  --band:#3c4b4a;
  --strip:#0d1414;
  --footer:#18262a;
  --footer-deep:#0a0f10;
  --white:#ffffff;
}
*{box-sizing:border-box;margin:0;padding:0}
html,body{width:1200px;height:2913px;overflow:hidden}
body{font-family:"Arimo",Arial,sans-serif;background:var(--white);color:var(--text);position:relative}

.utility-bar{height:23px;border-bottom:1px solid #e4e8e8;display:flex;justify-content:flex-end;align-items:center;gap:20px;padding-right:248px;font-size:9px;font-weight:700;color:var(--ink)}
.utility-bar a{display:flex;align-items:center;gap:5px;color:inherit;text-decoration:none}
.utility-bar .signup{color:var(--teal)}

.site-header{height:95px;display:flex;align-items:center;padding:0 248px}
.brand{display:flex;align-items:center;gap:10px;font-size:28px;font-weight:700;color:var(--teal);letter-spacing:2px}
.brand-dot{width:34px;height:34px;border-radius:50%;background:var(--teal)}
.header-tools{margin-left:auto;display:flex;align-items:center;gap:18px;font-size:10px;color:var(--ink)}
.tool{display:flex;align-items:center;gap:8px}
.tool-icon{width:34px;height:34px;border-radius:50%;border:1px solid #c9d3d3;display:flex;align-items:center;justify-content:center}
.search{width:166px;height:21px;border:1px solid #9aa6a6;border-radius:11px;display:flex;align-items:center;justify-content:space-between;padding:0 8px;font-size:9px;color:#777}

.main-nav{height:37px;background:linear-gradient(var(--teal-light),var(--teal));display:flex;justify-content:space-between;align-items:center;padding:0 270px 0 240px;font-size:9.5px;font-weight:700;color:var(--ink)}
.main-nav .active{color:var(--white)}

.about{padding:30px 248px 0;height:319px}
.section-title{font-size:22px;font-weight:700;letter-spacing:2px;color:var(--ink)}
.about-lead{margin-top:16px;font-size:12px;font-weight:700;letter-spacing:1.3px;line-height:24px;color:var(--ink)}
.about p{font-size:9.5px;line-height:18px;letter-spacing:.45px;margin-top:14px}

.team{background:var(--teal);height:1992px;padding:36px 248px 0}
.team .section-title{color:var(--white)}
.team-intro{margin-top:12px;width:500px;font-size:9.5px;font-weight:700;line-height:17px;color:var(--white);letter-spacing:.3px}
.team-grid{margin-top:30px;display:grid;grid-template-columns:repeat(3,224px);column-gap:15px;row-gap:15px}
.member{background:var(--white);height:348px;border-radius:3px;overflow:hidden;display:flex;flex-direction:column}
.member-photo{height:146px;background:linear-gradient(#ffffff,#e9eded)}
.member-name{height:18px;background:var(--band);color:var(--white);font-size:10px;font-weight:700;text-align:center;line-height:18px}
.member-role{height:12px;background:var(--strip);color:#d6dede;font-size:7px;text-align:center;line-height:12px;letter-spacing:.8px;text-transform:uppercase}
.member-bio{padding:8px 6px 0;font-size:9.5px;line-height:19px;color:#3c4444;letter-spacing:.4px}

.site-footer{background:linear-gradient(var(--footer),#0f1a1c);height:344px;padding-top:38px;color:var(--white)}
.footer-about{width:584px;margin-left:308px;font-size:10px;font-weight:700;line-height:20px;letter-spacing:.3px}
.divider{width:230px;height:1px;margin:34px auto 0;background:linear-gradient(90deg,transparent,#7e8c8c,transparent)}
.contacts{display:flex;margin:36px 0 0 308px;font-size:10px;font-weight:700;line-height:17px}
.contact{display:flex;gap:10px;align-items:flex-start}
.contact.address{width:246px}
.contact.phone{width:204px}
.social{display:flex;justify-content:center;gap:17px;margin-top:44px}
.social span{width:37px;height:37px;border:2px solid var(--white);border-radius:50%}
.bottom-bar{height:103px;background:var(--footer-deep);display:flex;align-items:center;justify-content:center;gap:12px;color:var(--white);font-size:10px;font-weight:700;line-height:16px}
.bottom-bar .mark{width:14px;height:14px;border-radius:50%;background:var(--white)}
</style>
</head>
<body>

<div class="utility-bar">
  <a class="signup" href="#"><svg width="14" height="12" viewBox="0 0 14 12"><rect x="1" y="2" width="9" height="9" fill="none" stroke="#2aa7a0" stroke-width="1.4"/><path d="M6 7l6-6" stroke="#2aa7a0" stroke-width="1.6"/></svg>SIGN UP</a>
  <a href="#"><svg width="12" height="12" viewBox="0 0 12 12"><rect x="1" y="5" width="9" height="7" fill="#1d2b2b"/><path d="M3 5V3a3 3 0 0 1 6 0" fill="none" stroke="#1d2b2b" stroke-width="1.5"/></svg>LOGIN</a>
  <a href="#"><svg width="14" height="12" viewBox="0 0 14 12"><path d="M0 1h3l2 7h7l2-5H4" fill="#1d2b2b" stroke="#1d2b2b"/><circle cx="6" cy="10.5" r="1.3" fill="#1d2b2b"/><circle cx="11" cy="10.5" r="1.3" fill="#1d2b2b"/></svg>CART</a>
</div>

<header class="site-header">
  <div class="brand"><span class="brand-dot"></span>QONDIMEX</div>
  <div class="header-tools">
    <div class="tool"><span class="tool-icon"><svg width="18" height="16" viewBox="0 0 18 16"><path d="M9 1C4.6 1 1 3.8 1 7.2c0 1.8 1 3.4 2.6 4.5L3 15l4-2.2c.6.1 1.3.2 2 .2 4.4 0 8-2.8 8-6S13.4 1 9 1z" fill="#2aa7a0"/></svg></span>LIVE CHAT</div>
    <div class="tool"><span class="tool-icon"><svg width="16" height="16" viewBox="0 0 16 16"><path d="M3 1l3 3-1.5 2c1 2 3 4 5 5l2-1.5 3 3-2 2C6 14 2 10 1 3z" fill="#2aa7a0"/></svg></span>213-555-0147</div>
    <div class="search">Search<svg width="10" height="10" viewBox="0 0 10 10"><circle cx="4" cy="4" r="3" fill="none" stroke="#777" stroke-width="1.2"/><path d="M6.3 6.3L9 9" stroke="#777" stroke-width="1.4"/></svg></div>
  </div>
</header>

<nav class="main-nav">
  <span>SERVERS</span><span>WORKSTATIONS</span><span>COMPONENTS</span><span>VIRTUAL REALITY</span><span>DRONES</span><span class="active">ABOUT US</span><span>BLOG</span><span>RESOURCES</span><span>CONTACT US</span>
</nav>

<section class="about">
  <h1 class="section-title">ABOUT US</h1>
  <h2 class="about-lead">QONDIMEX, LLC PROVIDES ENTERPRISE IT HARDWARE IN THE SAME QUALITY OF SERVICE AND EQUIPMENT THAT MAJOR BRANDS PROVIDE WITHOUT THE MAJOR BRAND PRICING.</h2>
  <p>We strive to deliver an alternate source for clients to obtain major brand hardware such as Dornell™, Harlow™, and Ixtra® at discounted rates and faster response times. Because the core of Enterprise class equipment revolves around reliability, our on-site testing facility fully examines all equipment to ensure that all hardware shipped and received succeeds industry standards for quality control.</p>
  <p>Our excellent customer service, top grade equipment coupled with our 3-year comprehensive warranty on configured machines allowed us to successfully develop a network of over 18,000 clients ranging from individual IT consultants to top enterprise companies. With our dedicated employees and 10,000 square foot warehouse we are able to provide countless configurations of Servers, Storages, and Workstations to businesses worldwide within a 72 hour time-frame. We are confident that we can fulfill all of your IT needs!</p>
</section>

<section class="team">
  <h2 class="section-title">MET THE TEAM</h2>
  <p class="team-intro">Curabitur et consequat tellus. Quisque volutpat aliquet rhoncus. Praesent sit amet enim eu leo pellentesque pellentesque eget vitae lacus. Nulla orci diam, aliquet eget dictum ultrices, venenatis sit amet augue. Sed dui metus, molestie vitae convallis ut, gravida at mauris.</p>

  <div class="team-grid">
    <article class="member"><div class="member-photo" role="img" aria-label="Portrait of Marisa Okonjo"></div><div class="member-name">Marisa Okonjo</div><div class="member-role">System Engineer</div><p class="member-bio">Leverage agile frameworks to provide a robust synopsis for high level overviews. Iterative approaches to corporate strategy foster collaborative thinking to further the overall value proposition. Organically grow the holistic world view of disruptive innovation via workplace diversity and empowerment.</p></article>

    <article class="member"><div class="member-photo" role="img" aria-label="Portrait of Tamsin Rell"></div><div class="member-name">Tamsin Rell</div><div class="member-role">Technical Support</div><p class="member-bio">Bring to the table win-win survival strategies to ensure proactive domination. At the end of the day, going forward, a new normal that has evolved from generation X is on the runway heading towards a streamlined cloud solution. User generated content is real-time will have multiple touchpoints.</p></article>

    <article class="member"><div class="member-photo" role="img" aria-label="Portrait of Orrin Kasdell"></div><div class="member-name">Orrin Kasdell</div><div class="member-role">Area Sales Manager</div><p class="member-bio">Capitalize on low hanging fruit to identify a ballpark value added activity to beta test. Override the digital divide with additional clickthroughs from DevOps. Nanotechnology immersion along the information highway will close the loop on focusing solely on the bottom line.</p></article>

    <article class="member"><div class="member-photo" role="img" aria-label="Portrait of Idris Vantholt"></div><div class="member-name">Idris Vantholt</div><div class="member-role">Web Developer</div><p class="member-bio">Podcasting operational change management inside of workflows to establish a framework. Taking seamless key performance indicators offline to maximise the long tail. Keeping your eye on the ball while performing a deep dive on the start-up mentality to derive convergence on cross-platform.</p></article>

    <article class="member"><div class="member-photo" role="img" aria-label="Portrait of Lenka Marrow"></div><div class="member-name">Lenka Marrow</div><div class="member-role">System Administrator</div><p class="member-bio">Collaboratively administrate empowered markets via plug-and-play networks. Dynamically procrastinate B2C users after installed base benefits. Dramatically visualize customer directed convergence without revolutionary ROI.</p></article>

    <article class="member"><div class="member-photo" role="img" aria-label="Portrait of Callum Breck"></div><div class="member-name">Callum Breck</div><div class="member-role">Support Representative</div><p class="member-bio">Efficiently unleash cross-media information without cross-media value. Quickly maximize timely deliverables for real-time schemas. Dramatically maintain clicks-and-mortar solutions without functional solutions.</p></article>

    <article class="member"><div class="member-photo" role="img" aria-label="Portrait of Noemi Farrant"></div><div class="member-name">Noemi Farrant</div><div class="member-role">Customer Service</div><p class="member-bio">Completely synergize resource taxing relationships via premier niche markets. Professionally cultivate one-to-one customer service with robust ideas. Dynamically innovate resource-leveling customer service for state of the art customer service.</p></article>

    <article class="member"><div class="member-photo" role="img" aria-label="Portrait of Greta Valloni"></div><div class="member-name">Greta Valloni</div><div class="member-role">Senior Systems Administrator</div><p class="member-bio">Objectively innovate empowered manufactured products whereas parallel platforms. Holisticly predominate extensible testing procedures for reliable supply chains. Dramatically engage top-line web services vis-a-vis cutting-edge deliverables.</p></article>

    <article class="member"><div class="member-photo" role="img" aria-label="Portrait of Anand Rijsdale"></div><div class="member-name">Anand Rijsdale</div><div class="member-role">Area Sales Manager</div><p class="member-bio">Proactively envisioned multimedia based expertise and cross-media growth strategies. Seamlessly visualize quality intellectual capital without superior collaboration and idea-sharing. Holistically pontificate installed base portals after maintainable products.</p></article>

    <article class="member"><div class="member-photo" role="img" aria-label="Portrait of Priya Desmane"></div><div class="member-name">Priya Desmane</div><div class="member-role">Support Representative</div><p class="member-bio">Credibly innovate granular internal or "organic" sources whereas high standards in web-readiness. Energistically scale future-proof core competencies vis-a-vis impactful experiences. Dramatically synthesize integrated schemas with optimal networks.</p></article>

    <article class="member"><div class="member-photo" role="img" aria-label="Portrait of Dorian Pell"></div><div class="member-name">Dorian Pell</div><div class="member-role">Area Sales Manager</div><p class="member-bio">Collaboratively administrate turnkey channels whereas virtual e-tailers. Objectively seize scalable metrics whereas proactive e-services. Seamlessly empower fully researched growth strategies and interoperable internal or "organic" sources.</p></article>

    <article class="member"><div class="member-photo" role="img" aria-label="Portrait of Ansel Quirado"></div><div class="member-name">Ansel Quirado</div><div class="member-role">Technical Support</div><p class="member-bio">Phosfluorescently engage worldwide methodologies with web-enabled technology. Interactively coordinate proactive e-commerce via process-centric "outside the box" thinking. Completely pursue scalable customer service through sustainable potentialities.</p></article>

    <article class="member"><div class="member-photo" role="img" aria-label="Portrait of Jae-won Sallow"></div><div class="member-name">Jae-won Sallow</div><div class="member-role">Support Representative</div><p class="member-bio">Interactively procrastinate high-payoff content without backward-compatible data. Quickly cultivate optimal processes and tactical architectures. Completely iterate covalent strategic theme areas via accurate e-markets.</p></article>
  </div>
</section>

<footer class="site-footer">
  <p class="footer-about">Based in Brindle Park California, Qondimex offers custom servers, storage, and workstations for local businesses in Harlan Heights, Westmere, Cobalt Bay, Fennwick, Ardley County, Sorrel Point, Marlow Glen, Vesper, Ottery, and Lindmoor. Qondimex also offers such products to clients throughout the United States and Worldwide.</p>
  <div class="divider"></div>
  <div class="contacts">
    <div class="contact address"><svg width="12" height="16" viewBox="0 0 12 16"><path d="M6 0a6 6 0 0 0-6 6c0 4 6 10 6 10s6-6 6-10a6 6 0 0 0-6-6z" fill="#fff"/><circle cx="6" cy="6" r="2.2" fill="#18262a"/></svg><span>4120 Larkfield Ave.<br>Brindle Park, CA 90871</span></div>
    <div class="contact phone"><svg width="16" height="16" viewBox="0 0 16 16"><path d="M3 1l3 3-1.5 2c1 2 3 4 5 5l2-1.5 3 3-2 2C6 14 2 10 1 3z" fill="#fff"/></svg><span>213-555-0147</span></div>
    <div class="contact"><svg width="18" height="13" viewBox="0 0 18 13"><rect width="18" height="13" rx="1" fill="#fff"/><path d="M1 1l8 6 8-6" fill="none" stroke="#18262a" stroke-width="1.5"/></svg><span>sales@qondimex.com</span></div>
  </div>
  <div class="divider"></div>
  <div class="social"><span></span><span></span><span></span><span></span></div>
</footer>

<div class="bottom-bar"><span class="mark"></span><span>Qondimex, LLC.<br>Copyright © 2017</span></div>

</body>
</html>
```